Quillbrook painting

Am looking for a lawn sign design for my paintings company.
I also attached my business card a example

Phone number of the business +1(204)555-0179
Key words:Free estimates|pressure washing |Residential| Commercial | Interior | Exterior

```html
<!DOCTYPE html>
<html lang="en">
<head>
<meta charset="UTF-8">
<title>Quillbrook Painting – Lawn Sign</title>
<link href="https://fonts.googleapis.com/css2?family=Signika:wght@500;600;700&display=swap" rel="stylesheet">
<style>
  :root {
    --canvas-bg: #b3b3b3;
    --sign-black: #030308;
    --paint-light: #62c9ee;
    --paint-deep: #0a92d6;
    --brand-blue: #17a6dc;
    --band-white: #ffffff;
    --ink: #050505;
    --handle-tan: #e8b88a;
    --ferrule-grey: #c9cbcf;
  }
  html, body {
    margin: 0;
    padding: 0;
    width: 1200px;
    height: 1084px;
    overflow: hidden;
    background: var(--canvas-bg);
  }
  .lawn-sign {
    position: absolute;
    left: 50px;
    top: 129px;
    width: 1100px;
    height: 826px;
    display: block;
  }
  .brand-name {
    font-family: "Signika", sans-serif;
    font-weight: 600;
    fill: var(--brand-blue);
    text-anchor: middle;
  }
  .service-list {
    font-family: "Signika", sans-serif;
    font-weight: 700;
    font-size: 43px;
    fill: var(--ink);
    text-anchor: end;
  }
  .phone-number {
    font-family: "Signika", sans-serif;
    font-weight: 700;
    font-size: 104px;
    fill: var(--brand-blue);
    text-anchor: middle;
  }
</style>
</head>
<body>
<svg class="lawn-sign" viewBox="0 0 906 680" xmlns="http://www.w3.org/2000/svg" aria-label="Quillbrook Painting lawn sign">
  <defs>
    <linearGradient id="washFill" x1="0" y1="0" x2="0" y2="1">
      <stop offset="0" stop-color="var(--paint-light)"/>
      <stop offset="1" stop-color="var(--paint-deep)"/>
    </linearGradient>
    <linearGradient id="brushFill" x1="0" y1="0" x2="1" y2="1">
      <stop offset="0" stop-color="var(--handle-tan)"/>
      <stop offset="1" stop-color="var(--ferrule-grey)"/>
    </linearGradient>
  </defs>

  <rect class="sign-panel" x="0" y="0" width="906" height="680" fill="var(--sign-black)"/>

  <g class="brush-and-paint-illustration" role="img" aria-label="Illustration of a paintbrush sweeping a wide stroke of blue paint across the sign">
    <rect x="150" y="186" width="756" height="336" fill="url(#washFill)"/>
    <rect x="0" y="0" width="240" height="230" fill="url(#brushFill)"/>
  </g>

  <text class="brand-name" x="473" y="96" font-size="52" textLength="416" lengthAdjust="spacingAndGlyphs">QUILLBROOK</text>
  <text class="brand-name" x="469" y="144" font-size="38" textLength="298" lengthAdjust="spacing">PAINTING</text>

  <g class="service-list">
    <text x="839" y="314">Free estimates</text>
    <text x="839" y="364">Pressure washing | Residential</text>
    <text x="839" y="414">Commercial | Interior</text>
    <text x="839" y="464">Exterior</text>
  </g>

  <rect class="phone-band" x="0" y="522" width="906" height="134" fill="var(--band-white)"/>
  <text class="phone-number" x="452" y="619" textLength="767" lengthAdjust="spacingAndGlyphs">+1(204)555-0179</text>

  <path class="footer-accent" fill="var(--paint-deep)"
        d="M490,680 L490,670 Q490,656 504,656 L906,656 L906,680 Z"/>
</svg>
</body>
</html>
```